Defense contractor needs a roll-up for an exhibition

The booth we have booked has only a size of 3m².
So this will be the centerpiece of the whole booth.
We need a roll-up that attracts visitors and at the same time it should contain already designed graphics. These graphics are giving visitors an overview of our system. So it is necessary to have them exposed in a height that the booth personal can conveniently point with its fingers at them.
For information about our company and product visit:
https://www.corvantilmetrics.com/
For designing you should use Adobe Illustrator and the templates provided in the zip file, to guarantee a perfect print.
I have supplied my business card that you can copy the logo. As the company logo will be already at the booth nearby the top of the roll-up, you should not place it there. It can be in the middle or at the bottom.
I have uploaded a picture of the booth. The roll up will be placed at the left of the screen and has a size of 80cm x 200cm

Defense

Defense

Serif

0054AA
0677BA
7BADD7
CADEEF
E8F1F8

Must have
• you must use the Adobe Illustrator template to have a good printing result
Should not have
• company logo on the upper side of the roll-up

```html
<!DOCTYPE html>
<html lang="en">
<head>
<meta charset="utf-8">
<title>Corvantil Metrics – Roll-up</title>
<link rel="stylesheet" href="https://fonts.googleapis.com/css2?family=Roboto+Condensed:ital,wght@0,400;0,700;0,800;1,800&family=Arimo:wght@400&display=swap">
<style>
  :root {
    --page-bg: #e9ecef;
    --banner-white: #ffffff;
    --banner-grey: #e4e5e9;
    --ink: #111111;
    --chevron-shadow: #6d6e72;
    --sky-deep: #1d2f7a;
    --sky-mid: #4a5fb8;
    --sky-glow: #c98aa4;
    --ground: #0d0d10;
    --art-light: #eceef5;
    --art-mid: #c3c8de;
    --art-shade: #8f9ad0;
  }
  * { margin: 0; padding: 0; box-sizing: border-box; }
  html, body { width: 1200px; height: 1173px; overflow: hidden; }
  body {
    background: var(--page-bg);
    display: flex; justify-content: center; align-items: center;
  }
  .rollup {
    position: relative;
    width: 453px; height: 1139px;
    background: linear-gradient(180deg, var(--banner-white) 45%, var(--banner-grey) 100%);
    box-shadow: 0 6px 24px rgba(0,0,0,.18);
    overflow: hidden;
  }
  .hero-photo {
    position: absolute; left: 0; top: 0; width: 100%; height: 170px;
    background:
      linear-gradient(180deg, transparent 70%, var(--ground) 100%),
      radial-gradient(ellipse 60% 45% at 50% 50%, var(--sky-glow) 0%, transparent 70%),
      linear-gradient(180deg, var(--sky-deep) 0%, var(--sky-mid) 55%, var(--sky-glow) 100%);
  }
  .headline-band { position: absolute; left: 0; top: 160px; width: 100%; height: 302px; }
  .headline {
    position: absolute; left: 0; top: 204px; width: 100%;
    text-align: center; color: #fff;
    font: italic 800 37px/44px "Roboto Condensed", sans-serif;
    text-transform: uppercase; letter-spacing: .2px;
  }
  .company-name {
    position: absolute; left: 33px; top: 486px;
    display: flex; align-items: center; gap: 10px;
    font: 800 31px/1 "Roboto Condensed", sans-serif;
    text-transform: uppercase; color: var(--ink);
  }
  .company-name .mark { width: 16px; height: 16px; background: var(--ink); }
  .system-overview {
    position: absolute; left: 18px; top: 538px; width: 417px; height: 278px;
    background:
      radial-gradient(ellipse 40% 30% at 75% 70%, var(--art-shade) 0%, transparent 75%),
      radial-gradient(ellipse 30% 25% at 22% 35%, var(--art-mid) 0%, transparent 80%),
      radial-gradient(ellipse 35% 15% at 70% 12%, var(--art-mid) 0%, transparent 80%),
      linear-gradient(180deg, var(--art-light) 0%, rgba(236,238,245,0) 100%);
  }
  .services { position: absolute; left: 30px; top: 818px; width: 400px; color: var(--ink); }
  .services h2 {
    font: 700 27px/1 "Roboto Condensed", sans-serif;
    display: inline-block; padding-bottom: 6px; border-bottom: 2px solid var(--ink);
    padding-right: 46px; margin-bottom: 12px;
  }
  .services .intro { font: 700 16px/19px "Roboto Condensed", sans-serif; margin-bottom: 10px; }
  .services ul { list-style: none; margin-bottom: 12px; }
  .services li {
    display: flex; align-items: center; gap: 11px;
    font: 400 17px/20px "Arimo", sans-serif;
  }
  .services li svg { width: 15px; height: 15px; flex: none; }
  .services .closing { font: 700 17px/20px "Roboto Condensed", sans-serif; }
</style>
</head>
<body>
  <main class="rollup">
    <div class="hero-photo" role="img" aria-label="Silhouette of a battle tank on a grassy ridge against a blue and pink sunset sky"></div>

    <svg class="headline-band" viewBox="0 0 453 302" preserveAspectRatio="none" aria-hidden="true">
      <polygon points="0,212 453,212 453,240 226,302 0,240" fill="var(--chevron-shadow)"/>
      <polygon points="0,0 453,0 453,224 226,292 0,224" fill="var(--ink)"/>
    </svg>

    <h1 class="headline">Advanced combat<br>training systems for<br>realistic combat<br>simulation</h1>

    <div class="company-name"><span class="mark"></span>Corvantil Metrics</div>

    <div class="system-overview" role="img" aria-label="Isometric system overview: two tanks, three target stations and a command truck with operators and monitors"></div>

    <section class="services">
      <h2>Services</h2>
      <p class="intro">The signature of the contract is not the end<br>it is just the beginning of a long-lasting partnership.<br>We offer</p>
      <ul>
        <li><svg viewBox="0 0 14 14"><circle cx="7" cy="7" r="5.5" fill="none" stroke="currentColor" stroke-width="1.3"/><path d="M4 7l2.3 2.3L12 2.5" fill="none" stroke="currentColor" stroke-width="1.6"/></svg>extended warranty programs</li>
        <li><svg viewBox="0 0 14 14"><circle cx="7" cy="7" r="5.5" fill="none" stroke="currentColor" stroke-width="1.3"/><path d="M4 7l2.3 2.3L12 2.5" fill="none" stroke="currentColor" stroke-width="1.6"/></svg>logistics support</li>
        <li><svg viewBox="0 0 14 14"><circle cx="7" cy="7" r="5.5" fill="none" stroke="currentColor" stroke-width="1.3"/><path d="M4 7l2.3 2.3L12 2.5" fill="none" stroke="currentColor" stroke-width="1.6"/></svg>maintenance contracts</li>
        <li><svg viewBox="0 0 14 14"><circle cx="7" cy="7" r="5.5" fill="none" stroke="currentColor" stroke-width="1.3"/><path d="M4 7l2.3 2.3L12 2.5" fill="none" stroke="currentColor" stroke-width="1.6"/></svg>long-term spare part services</li>
      </ul>
      <p class="closing">to keep the equipment in perfect operational condition</p>
    </section>
  </main>
</body>
</html>
```